Funeral Services Site

We need a website for a Funeral Services company. The old website is: www.rouwcentrumdelvoort.be We need the same structure and text.

Target Market(s)

Customers.

Coding

Coded - Design and coding required

Number of Pages Required

4 page

Font styles to use
Serif
Sans Serif
Script

```html
<!DOCTYPE html>
<html lang="en">
<head>
<meta charset="utf-8">
<title>Funeral Home Delvoort Bvba</title>
<link href="https://fonts.googleapis.com/css2?family=Poppins:wght@300;400;500;600&display=swap" rel="stylesheet">
<style>
:root{
  --gold:#d8ab74;
  --ink:#2f2f2f;
  --text:#333;
  --grey-bg:#f3f3f3;
  --dark:#393939;
  --white:#fff;
  --field-border:#d6d6d6;
}
*{margin:0;padding:0;box-sizing:border-box}
html,body{width:1200px;height:2754px;overflow:hidden}
body{font-family:'Poppins',sans-serif;color:var(--text);background:var(--white);position:relative}
.abs{position:absolute}
.center{left:0;width:1200px;text-align:center}

/* header */
.header{top:0;left:0;width:1200px;height:111px;background:var(--white)}
.brand{left:142px;top:20px;display:flex;align-items:center;gap:12px}
.brand-dot{width:76px;height:76px;border-radius:50%;background:#222}
.brand-name{font-size:25px;line-height:30px;color:var(--ink);font-weight:400}
.top-phone{right:148px;top:12px;display:flex;align-items:center;gap:10px;font-size:16px;font-weight:500;color:var(--ink)}
.nav{right:148px;top:70px;display:flex;gap:36px;font-size:16px;color:var(--ink)}
.nav .active{color:var(--gold)}

/* hero */
.hero{top:111px;left:0;width:1200px;height:600px;overflow:hidden}
.hero-photo{position:absolute;inset:0;background:linear-gradient(135deg,#5d5a4c 0%,#3a3d34 35%,#6e6a62 60%,#2c3a2e 100%)}
.hero-title{top:290px;font-size:34px;line-height:48px;color:var(--white);font-weight:400}
.pill{display:inline-flex;align-items:center;gap:14px;background:var(--gold);color:var(--white);border-radius:24px;font-size:17px}
.hero-cta{top:398px;left:423px;height:44px;padding:0 24px}
.arrow-btn{top:391px;width:34px;height:28px;background:#555;border:2px solid #ccc;display:flex;align-items:center;justify-content:center}

h2.section-title{font-size:34px;font-weight:400;color:var(--ink)}
.rule{height:2px;width:86px;background:var(--ink);margin:6px auto 0}
.gold-sub{color:var(--gold);font-size:17px}
.body-text{font-size:13.5px;line-height:24px;color:var(--text)}
.btn{display:inline-block;background:var(--gold);color:var(--white);border-radius:18px;font-weight:500}

/* worship */
.worship-bg{top:1100px;left:0;width:1200px;height:420px;background:var(--grey-bg)}
.card{top:1415px;width:298px;height:238px;overflow:hidden}
.card-photo{position:absolute;inset:0}
.card-caption{position:absolute;left:0;bottom:0;width:100%;height:57px;background:rgba(40,40,40,.55);color:var(--white);font-size:15.5px;line-height:22px;padding:6px 8px;white-space:nowrap}
.card-caption.tight{font-size:14px;letter-spacing:-0.2px}

/* form */
.field{position:absolute;border:1px solid var(--field-border);background:var(--white);font-size:11px;font-weight:600;color:#333;padding:6px 15px}

/* cta band */
.cta-band{top:2187px;left:0;width:1200px;height:256px;background:var(--grey-bg)}
.cta-text{font-size:19.5px;line-height:36px;color:var(--ink);text-transform:uppercase}

/* footer */
.footer{top:2443px;left:0;width:1200px;height:266px;background:var(--dark);color:var(--white)}
.foot-head{font-size:15.5px}
.foot-rule{width:38px;height:2px;background:var(--white);margin-top:6px}
.foot-links{list-style:none;font-size:12.5px;line-height:27.5px;margin-top:12px}
.foot-item{display:flex;gap:12px;font-size:12.5px;line-height:21px}
.foot-brand{font-size:28px;line-height:32px;color:var(--white);font-weight:400;text-align:right}
.copyright{top:2709px;height:45px;background:var(--gold);color:var(--white);font-size:12.5px;line-height:45px}
</style>
</head>
<body>

<header class="abs header">
  <div class="abs brand">
    <div class="brand-dot"></div>
    <div class="brand-name">Funeral Home<br>Delvoort Bvba:</div>
  </div>
  <div class="abs top-phone">
    <svg width="24" height="24" viewBox="0 0 24 24" fill="none" stroke="#222" stroke-width="1.8"><circle cx="12" cy="12" r="10.5"/><path d="M8 6.5l2 2.5-1.2 1.5c.8 1.8 2 3 3.8 3.8l1.5-1.2 2.5 2-1.2 2c-4-.5-8-4.5-8.6-8.6z" fill="#222"/></svg>
    1-555-240-8100
  </div>
  <nav class="abs nav">
    <span class="active">Home</span><span>About Us</span><span>Condole Online</span><span>Order Flowers</span><span>Contact Us</span>
  </nav>
</header>

<section class="abs hero">
  <div class="hero-photo" role="img" aria-label="Hands placing flowers on a grave"></div>
  <svg class="abs" style="left:0;top:400px" width="1200" height="200" viewBox="0 0 1200 200">
    <path d="M0 106 Q600 262 1200 106 L1200 200 L0 200 Z" fill="#fff"/>
    <path d="M0 110 Q600 266 1200 110" fill="none" stroke="var(--gold)" stroke-width="5"/>
  </svg>
</section>
<h1 class="abs center hero-title">Funeral Home Delvoort Bvba:<br>A Personal Service In Farewell Guidance</h1>
<div class="abs pill hero-cta">Contact Us Today
  <svg width="24" height="24" viewBox="0 0 24 24" fill="none" stroke="#fff" stroke-width="1.8"><circle cx="12" cy="12" r="10.5"/><path d="M8 6.5l2 2.5-1.2 1.5c.8 1.8 2 3 3.8 3.8l1.5-1.2 2.5 2-1.2 2c-4-.5-8-4.5-8.6-8.6z" fill="#fff"/></svg>
  1-555-240-8100</div>
<div class="abs arrow-btn" style="left:0"><svg width="10" height="12"><path d="M7 1L2 6l5 5" stroke="#fff" stroke-width="2" fill="none"/></svg></div>
<div class="abs arrow-btn" style="right:0"><svg width="10" height="12"><path d="M3 1l5 5-5 5" stroke="#fff" stroke-width="2" fill="none"/></svg></div>

<!-- about -->
<div class="abs center" style="top:765px"><h2 class="section-title">About Us</h2><div class="rule"></div></div>
<p class="abs center gold-sub" style="top:833px">Mourning Center Delvoort, A Complete Service In Mourning And Farewell Guidance</p>
<p class="abs center body-text" style="top:864px;left:150px;width:900px">Saying goodbye to a loved one is one of the toughest things in a lifetime. Funeral home Delvoort in Beekdal takes care of all the practical and administrative matters involved. So you can say goodbye in peace.</p>
<p class="abs center body-text" style="top:916px;left:150px;width:900px">Our people have a r uime experience in farewell guidance and stand for 24 hours at 24 hours for you. Our fully renovated funeral home is open to you and your acquaintances, so that you can greet your loved one at any time of the day.</p>
<div class="abs btn" style="top:977px;left:543px;width:113px;height:32px;line-height:32px;text-align:center;font-size:15.5px">Read More</div>

<!-- worship -->
<div class="abs worship-bg"></div>
<svg class="abs" style="left:0;top:1460px" width="1200" height="80" viewBox="0 0 1200 80"><path d="M0 25 Q600 -30 1200 25 L1200 80 L0 80 Z" fill="#fff"/></svg>
<div class="abs center" style="top:1151px"><h2 class="section-title">Organization Funeral And Worship</h2><div class="rule" style="width:120px"></div></div>
<p class="abs center body-text" style="top:1219px;left:170px;width:860px;line-height:25.5px">The organization of the funeral ceremony is a moment of reflection, where the personality of the deceased can be beautifully highlighted. Our team will assist you in this and select the most beautiful texts, songs and photos with you in order to arrive at an appropriate and worthy goodbye.</p>
<p class="abs center body-text" style="top:1307px">The funeral can take place in your parish church or &nbsp;our auditorium if you wish, which can accommodate a maximum of 100 guests.</p>
<p class="abs center gold-sub" style="top:1347px;font-weight:500">We Can Arrange The Following For You:</p>

<div class="abs card" style="left:141px"><div class="card-photo" role="img" aria-label="Mourners beside a casket with flowers" style="background:linear-gradient(120deg,#c9bfae,#6a4d3a 55%,#2d2622)"></div><div class="card-caption">Vigil The Night Before<br>The Funeral</div></div>
<div class="abs card" style="left:451px"><div class="card-photo" role="img" aria-label="Prayer service with clergy in a church" style="background:linear-gradient(120deg,#8a6a4f,#b53a32 55%,#3a2a22)"></div><div class="card-caption">Prayer Service With Priest<br>(if Possible)</div></div>
<div class="abs card" style="left:761px"><div class="card-photo" role="img" aria-label="Priest at a eucharistic celebration" style="background:linear-gradient(120deg,#6b5530,#c8a35a 50%,#4a3a26)"></div><div class="card-caption tight">Eucharistic Celebration With Priest (on<br>Tue. &amp; Fri. In The Parishes of Beekdal)</div></div>

<!-- quick contact -->
<div class="abs center" style="top:1733px"><h2 class="section-title">Quick Contact</h2><div class="rule" style="width:68px"></div></div>
<p class="abs center body-text" style="top:1802px;left:160px;width:880px">Lorem ipsum dolor sit amet, consectetuer adipiscing elit, sed diam nonummy nibh euismod tincidunt ut laoreet dolore magna aliquam erat volutpat. Ut wisi enim ad minim veniam.</p>
<div class="field" style="left:302px;top:1854px;width:290px;height:38px">First Name</div>
<div class="field" style="left:608px;top:1854px;width:290px;height:38px;padding-top:18px">Last Name</div>
<div class="field" style="left:302px;top:1906px;width:290px;height:38px">Email</div>
<div class="field" style="left:608px;top:1906px;width:290px;height:38px;padding-top:18px">Phone</div>
<div class="field" style="left:302px;top:1962px;width:596px;height:86px;padding-top:10px">Message</div>
<div class="abs btn" style="top:2070px;left:538px;width:100px;height:31px;line-height:31px;text-align:center;font-size:14px">SUBMIT</div>

<!-- cta band -->
<div class="abs cta-band"></div>
<p class="abs center cta-text" style="top:2244px">Do you have any questions <span style="color:var(--gold)">or</span> would you like to call in our funeral home?<br>Contact us. We are here for you.</p>
<div class="abs pill" style="top:2331px;left:417px;height:44px;padding:0 22px">Contact Us Today
  <svg width="24" height="24" viewBox="0 0 24 24" fill="none" stroke="#fff" stroke-width="1.8"><circle cx="12" cy="12" r="10.5"/><path d="M8 6.5l2 2.5-1.2 1.5c.8 1.8 2 3 3.8 3.8l1.5-1.2 2.5 2-1.2 2c-4-.5-8-4.5-8.6-8.6z" fill="#fff"/></svg>
  1-555-240-8100</div>

<!-- footer -->
<footer class="abs footer">
  <div class="abs" style="left:145px;top:48px">
    <div class="foot-head">Quick Links</div><div class="foot-rule"></div>
    <ul class="foot-links"><li>Home</li><li>About Us</li><li>Condole Online</li><li>Order Flowers</li><li>Contact Us</li></ul>
  </div>
  <div class="abs" style="left:377px;top:50px">
    <div class="foot-head">Contact Details</div><div class="foot-rule"></div>
    <div class="foot-item" style="margin-top:18px">
      <svg width="14" height="20" viewBox="0 0 14 20"><path d="M7 1a6 6 0 0 0-6 6c0 4.5 6 12 6 12s6-7.5 6-12a6 6 0 0 0-6-6z" fill="var(--gold)"/><circle cx="7" cy="7" r="2.3" fill="var(--dark)"/></svg>
      <span>Funeral Home Delvoort Bvba:<br>Hoeveweg 18, 3700 Beekdal</span>
    </div>
    <div class="foot-item" style="margin-top:24px;align-items:center">
      <svg width="18" height="18" viewBox="0 0 24 24" fill="none" stroke="var(--gold)" stroke-width="1.8"><circle cx="12" cy="12" r="10.5"/><path d="M8 6.5l2 2.5-1.2 1.5c.8 1.8 2 3 3.8 3.8l1.5-1.2 2.5 2-1.2 2c-4-.5-8-4.5-8.6-8.6z" fill="var(--gold)"/></svg>
      <span>24/24, 7 out of 7 &nbsp;- 012 00 41 41</span>
    </div>
    <div class="foot-item" style="margin-top:20px;align-items:center">
      <svg width="18" height="13" viewBox="0 0 18 13" fill="none" stroke="var(--gold)" stroke-width="1.4"><rect x="1" y="1" width="16" height="11"/><path d="M1 1l8 6 8-6"/></svg>
      <span>mourningcenter.delvoort@example.com</span>
    </div>
  </div>
  <div class="abs" style="right:140px;top:112px;display:flex;align-items:center;gap:10px">
    <div class="foot-brand">Funeral home<br>Delvoort bvba</div>
    <div style="width:56px;height:56px;border-radius:50%;border:2px solid #fff"></div>
  </div>
</footer>
<div class="abs center copyright">Copyright © 2019 Northwind Media &nbsp;- Sitemap &nbsp;- Privacy Policy</div>

</body>
</html>
```